Real Estate flyer for listing properties

This is a flyer to be used by the property lister (the person trying to convince property vendors to sell through us) of our real estate agency Golden Harbour (https://www.golden-harbour.example). The aim of the flyer is to convince owners to list their properties with us, so that we can advertise & sell them. We have our offices located in San Luis de Sabinillas / Manilva, Costa del Sol, Spain. The real estate market here is highly competetive and we want to stand out from our competition and establish trust, which is essential for owners to list with us.

I have attached the design of our old flyer. Please note that we would like the new flyer to use our new logo, and our colors, not the wine red color used previously

I have also added some photos of our offices and of properties we have sold. We can provide more photos on request.

1. Project Overview & Objectives
High-level goal: Convince owners in Manilva & nearby to list with us.

2. Style guidelines
Please stick with the current logo & Font. We do NOT require a logo re-design. The font for Golden Harbour is Myriad Pro Bold Italic in color #D1672E. The blue used is #65A8DE and yellow #F2E946
The flyer should be A5 size.

3. Mandatory elements
Section with agent photo, name, email address & phone number. The design should allow for the flyer to be two sided, where one side is in English, and the other side in Spanish.

4. Ideas
- Maybe include address of offices (Calle Los Pinos 8, 29601 San Luis de Sabinillas) or QR code to open on google
- Offer free valuations
- Maybe mention biggest portals we are on with logo e.g. Casaverde, Vivilar, Techos.example, Moravo, A Home By the Bay, etc
- List languages we speak (Spanish, English, German, Russian, Ukrainian, Lithuanian, French, Italian, Danish, Polish)
- We also offer: Maintenance & Key holding
- Mention we have clients waiting
Note, these are just ideas, obviously not everything can be on the flyer.

Please note that the final flyer should be good for printing, just to be updated with the agents picture and contact details. Meaning all the marketing text should be written.

5. Assets & Output
Output sizes: e.g. A5 print flyer (210 × 148 mm), plus a social-media optimized JPG (1080 × 1080 px).

File formats required: InDesign (editable), plus flattened PDF for print; JPG/PNG for web.

5. Additional task - "stationary"
We need a design for a flap folder. I have attached a photo of such a flap folder, as well as the illustrator printing guidelines from the printing company.

Feel free to message me in case you have any questions or doubts.

Industry/Entity Type

Real Estate

Requirements
Must have
• Use our company logo, color scheme (from logo)

```html
<!DOCTYPE html>
<html lang="en">
<head>
<meta charset="utf-8">
<title>Golden Harbour – Sell With Us</title>
<link rel="stylesheet" href="https://fonts.googleapis.com/css2?family=Source+Sans+3:wght@400;600;700;800&display=swap">
<style>
  :root{
    --sand:#E9E8E3;
    --sun:#F6BD25;
    --sky:#5DA5DD;
    --terracotta:#D1672E;
    --ink:#111111;
    --slate:#555555;
    --white:#ffffff;
  }
  *{box-sizing:border-box;margin:0;padding:0}
  html,body{width:845px;height:1200px;overflow:hidden;background:var(--white)}
  body{font-family:"Source Sans 3",sans-serif;color:var(--ink)}
  .flyer{position:relative;width:845px;height:1200px;overflow:hidden;background:var(--white)}

  .hero{position:absolute;left:0;top:0;width:544px;height:528px;background:var(--sand);border-bottom-right-radius:60px}
  .brand{position:absolute;left:76px;top:70px;display:flex;align-items:center;gap:18px}
  .brand-dot{width:112px;height:112px;border-radius:50%;background:var(--sun);flex:none}
  .brand-name{font-weight:700;font-size:40px;line-height:1;color:var(--terracotta)}
  .brand-area{font-size:20px;color:var(--slate);margin-top:10px}
  .brand-url{font-size:20px;color:var(--slate);margin-top:6px;font-weight:700}

  .slogan{position:absolute;left:0;top:0;width:544px;height:528px}
  .slogan-row{position:absolute;display:flex;align-items:center;font-weight:700;font-size:68px;line-height:1;letter-spacing:-1px}
  .slogan-tag{color:var(--white);padding:4px 8px 8px;margin-right:10px}
  .row-smart{left:107px;top:218px;color:var(--sky)}
  .row-smart .slogan-tag{background:var(--sky);transform:rotate(-1deg)}
  .row-fast{left:138px;top:284px;color:var(--sun)}
  .row-fast .slogan-tag{background:var(--sun);transform:rotate(2deg)}
  .row-us{left:87px;top:364px;color:var(--terracotta)}
  .row-us .slogan-tag{background:var(--terracotta);transform:rotate(-1.5deg)}
  .hero-rule{position:absolute;left:216px;top:449px;width:126px;height:2px;background:var(--ink)}
  .hero-cta{position:absolute;left:0;width:544px;top:466px;text-align:center;font-weight:700;font-size:26px}

  .agent{position:absolute;left:556px;top:0;width:289px;height:432px;background:var(--sun);border-bottom-left-radius:40px}
  .agent-title{position:absolute;right:46px;top:44px;text-align:right;font-weight:700;font-size:18px;line-height:24px;text-transform:uppercase}
  .agent-photo{position:absolute;left:45px;top:150px;width:160px;height:160px;border-radius:50%;background:radial-gradient(circle at 50% 40%,#c8b8a8,#9a8a7c);border:3px solid var(--sand)}
  .hola{position:absolute;left:-50px;top:174px;width:112px;height:112px;border-radius:50%;background:#F2A531;display:flex;align-items:center;justify-content:center;color:var(--white);font-weight:800;font-size:25px;transform:rotate(-14deg)}
  .agent-contact{position:absolute;left:0;width:289px;top:324px;text-align:center;font-weight:700}
  .agent-name{font-size:18px;line-height:24px}
  .agent-phone{font-size:18px;line-height:24px}
  .agent-mail{font-size:14px;line-height:22px}

  .office-photo{position:absolute;left:556px;top:444px;width:289px;height:209px;border-top-left-radius:50px;background:linear-gradient(180deg,#b9c6d8 0%,#e2b797 55%,#6a6a70 100%)}
  .building-photo{position:absolute;left:0;top:540px;width:289px;height:660px;border-top-right-radius:60px;background:linear-gradient(180deg,#a9c6e4 0%,#f1f0ec 18%,#e4e2dd 70%,#45b3e0 88%,#2f9fd6 100%)}

  .question{position:absolute;left:301px;top:542px;width:243px;height:140px;border-radius:70px;background:var(--sun);display:flex;align-items:center;justify-content:center;text-align:center;font-weight:700;font-size:27px;line-height:32px}
  .pool-photo{position:absolute;left:301px;top:695px;width:243px;height:155px;border-radius:122px 122px 0 0;background:linear-gradient(180deg,#3c8fd6 0%,#d9e6f1 30%,#8fb36b 45%,#66b6e6 62%,#d9d3c5 100%)}
  .promise{position:absolute;left:301px;top:850px;width:243px;height:350px;background:var(--sun);text-align:center}
  .promise-head{margin-top:16px;font-weight:700;font-size:29px;line-height:32px}
  .promise-rule{width:64px;height:2px;background:var(--ink);margin:12px auto}
  .promise-line{font-size:19px;line-height:24px}
  .promise-text{font-size:18px;line-height:24px}
  .promise-text strong{font-weight:700}

  .benefits{position:absolute;left:556px;top:665px;width:289px;height:535px;background:var(--sand);border-top-left-radius:50px}
  .benefits-head{position:absolute;left:42px;top:20px;font-weight:700;font-size:42px;line-height:54px}
  .benefit{position:absolute;left:12px;display:flex;align-items:flex-start;gap:10px}
  .benefit-icon{width:46px;height:46px;border-radius:50%;background:var(--sun);display:flex;align-items:center;justify-content:center;flex:none;margin-top:10px}
  .benefit-text{font-size:19px;line-height:24px;width:220px}
</style>
</head>
<body>
<main class="flyer">

  <section class="hero">
    <div class="brand">
      <div class="brand-dot"></div>
      <div>
        <div class="brand-name">Golden Harbour</div>
        <div class="brand-area">Marbella Estepona Sotogrande</div>
        <div class="brand-url">www.golden-harbour.example</div>
      </div>
    </div>
    <div class="slogan">
      <div class="slogan-row row-smart"><span class="slogan-tag">Sell</span>smart.</div>
      <div class="slogan-row row-fast"><span class="slogan-tag">Sell</span>fast.</div>
      <div class="slogan-row row-us"><span class="slogan-tag">Sell</span>with us.</div>
    </div>
    <div class="hero-rule"></div>
    <p class="hero-cta">Let’s get started today!</p>
  </section>

  <aside class="agent">
    <h2 class="agent-title">Your property<br>specialist for<br>Estepona, Manilva &amp;<br>Sotogrande</h2>
    <div class="agent-photo" role="img" aria-label="Portrait photo of the property agent"></div>
    <div class="hola">Hola!</div>
    <div class="agent-contact">
      <p class="agent-name">Lucia Varela</p>
      <p class="agent-phone">(+34) 600 41 27 58</p>
      <p class="agent-mail">lucia@golden-harbour.example</p>
    </div>
  </aside>

  <div class="office-photo" role="img" aria-label="Photo of the agency office on a street corner at sunset"></div>
  <div class="building-photo" role="img" aria-label="Photo of a white apartment building with a swimming pool"></div>

  <div class="question">Selling Your Property on the Costa del Sol?</div>
  <div class="pool-photo" role="img" aria-label="Photo of a residential complex with a pool and palm trees"></div>

  <section class="promise">
    <h3 class="promise-head">We make it<br>easy, fast,<br>and profitable.</h3>
    <div class="promise-rule"></div>
    <p class="promise-line">Call 951 000 482</p>
    <p class="promise-line">sell@golden-harbour.example</p>
    <div class="promise-rule"></div>
    <p class="promise-text">We’ll come by, take<br>professional photos, and<br>provide a free valuation<br><strong>no strings attached.</strong></p>
  </section>

  <section class="benefits">
    <h2 class="benefits-head">Why Sell<br>With Us?</h2>

    <div class="benefit" style="top:134px">
      <span class="benefit-icon"><svg width="24" height="24" viewBox="0 0 24 24"><path d="M4 7h4l2-2h4l2 2h4v12H4z" fill="var(--ink)"/><circle cx="12" cy="13" r="3.5" fill="var(--sun)"/></svg></span>
      <p class="benefit-text">Stunning photos,<br>drone shots &amp; 360°<br>tours</p>
    </div>
    <div class="benefit" style="top:217px">
      <span class="benefit-icon"><svg width="26" height="24" viewBox="0 0 26 24"><rect x="2" y="4" width="12" height="11" rx="1" fill="var(--ink)"/><rect x="12" y="8" width="12" height="11" rx="1" fill="none" stroke="var(--ink)" stroke-width="2"/><path d="M5 13l3-7 3 7" stroke="var(--white)" stroke-width="1.5" fill="none"/></svg></span>
      <p class="benefit-text">Multilingual<br>descriptions &amp; top<br>visibility</p>
    </div>
    <div class="benefit" style="top:301px">
      <span class="benefit-icon"><svg width="26" height="26" viewBox="0 0 26 26"><circle cx="11" cy="11" r="8" fill="none" stroke="var(--ink)" stroke-width="2.2"/><path d="M17 17l6 6" stroke="var(--ink)" stroke-width="2.6"/><path d="M7 12l4-4 4 4v3H7z" fill="var(--ink)"/></svg></span>
      <p class="benefit-text">Listed with 2,000+<br>agencies + major<br>portals</p>
    </div>
    <div class="benefit" style="top:386px">
      <span class="benefit-icon"><svg width="26" height="24" viewBox="0 0 26 24"><path d="M3 10l6-5 4 3 4-3 6 5-9 9z" fill="none" stroke="var(--ink)" stroke-width="2" stroke-linejoin="round"/></svg></span>
      <p class="benefit-text">Full-service support /<br>even if you’re abroad</p>
    </div>
    <div class="benefit" style="top:445px">
      <span class="benefit-icon"><svg width="24" height="24" viewBox="0 0 24 24"><rect x="4" y="5" width="16" height="15" rx="2" fill="none" stroke="var(--ink)" stroke-width="2"/><path d="M4 9h16M8 3v4M16 3v4" stroke="var(--ink)" stroke-width="2"/><text x="12" y="18" font-size="8" font-weight="700" text-anchor="middle" fill="var(--ink)" font-family="sans-serif">7</text></svg></span>
      <p class="benefit-text">7-day availability,<br>including evening</p>
    </div>
  </section>

</main>
</body>
</html>
```